Caldwen Primary School

We need to improve on our designs for a local School, Caldwen Primary.
One file contains the correct information required on the sign.
Our Mock ups are suggestions.
The School Uniform is blue -
We had these comments from our Client.
I can't decide whether to change the blue and try green to represent our commitment to outdoors, or maybe a combination of colours from the school badge, For the main sign options , I like them both but wondered if there was a way of combining the two? Slightly bigger badge.

I've included the files for the smaller signs if you were happy to provide a service to include all. We are a sign business focusing on other projects and external support will help. Thanks - Oscar.

```html
<!DOCTYPE html>
<html lang="en">
<head>
<meta charset="utf-8">
<title>Caldwen Primary School – Signage</title>
<link rel="stylesheet" href="https://fonts.googleapis.com/css2?family=Outfit:wght@500;600;700&display=swap">
<style>
  :root {
    --school-blue: #1174bd;
    --outdoor-green: #22b14c;
    --sun-yellow: #f9e03f;
    --sun-orange: #f7941d;
    --white: #ffffff;
    --paper: #ffffff;
  }
  * { box-sizing: border-box; margin: 0; padding: 0; }
  html, body { width: 884px; height: 1200px; overflow: hidden; background: var(--paper); }
  body { font-family: "Outfit", sans-serif; position: relative; }

  .main-sign { position: absolute; left: 61px; top: 54px; width: 772px; height: 528px; }
  .main-sign__shape { position: absolute; inset: 0; }
  .badge { position: absolute; left: 0; right: 0; top: 28px; text-align: center; }
  .badge__dot { display: block; width: 88px; height: 88px; margin: 0 auto 10px; border-radius: 50%; background: var(--sun-orange); }
  .badge__name { color: var(--sun-yellow); font-weight: 700; font-size: 30px; letter-spacing: .5px; }

  .main-sign__title { position: absolute; left: 0; right: 0; top: 216px; text-align: center; color: var(--white); font-weight: 600; font-size: 58px; line-height: 70px; letter-spacing: -.5px; }
  .main-sign__motto { position: absolute; left: 0; right: 0; top: 370px; text-align: center; color: var(--sun-yellow); font-weight: 700; font-size: 31px; }

  .contact-band { position: absolute; left: 0; right: 0; top: 434px; height: 94px; display: flex; align-items: center; justify-content: center; gap: 18px; color: var(--white); }
  .contact-band__phone { font-weight: 600; font-size: 46px; letter-spacing: .5px; }
  .council-mark { position: absolute; right: 36px; top: 22px; width: 70px; text-align: center; color: var(--white); font-weight: 600; font-size: 11px; line-height: 13px; }
  .council-mark__square { display: block; width: 34px; height: 22px; margin: 3px auto; background: var(--white); }

  .panel-grid { position: absolute; left: 61px; top: 650px; width: 772px; display: grid; grid-template-columns: repeat(3, 249px); grid-auto-rows: 248px; column-gap: 12.5px; row-gap: 14px; }
  .panel { position: relative; background: var(--school-blue); border-radius: 11px; padding: 18px 16px 0 20px; }
  .panel__school { color: var(--white); font-weight: 600; font-size: 25px; line-height: 27px; }
  .panel__message { margin-top: 8px; color: var(--sun-yellow); font-weight: 700; font-size: 23px; line-height: 25px; }
  .panel__notes { margin-top: 10px; font-weight: 600; font-size: 14px; line-height: 18px; color: var(--white); }
  .panel__notes p { margin-bottom: 9px; }
  .panel__notes .panel__notes--alert { color: var(--sun-yellow); }
  .panel__arrow { position: absolute; left: 22px; bottom: 14px; width: 46px; height: 34px; }
</style>
</head>
<body>

<section class="main-sign">
  <svg class="main-sign__shape" viewBox="0 0 772 528" width="772" height="528" aria-hidden="true">
    <path d="M0 106 Q0 94 12 94 H274 A113 113 0 0 1 498 94 H760 Q772 94 772 106 V434 H0 Z" fill="var(--school-blue)"/>
    <path d="M0 434 H772 V516 Q772 528 760 528 H12 Q0 528 0 516 Z" fill="var(--outdoor-green)"/>
  </svg>

  <div class="badge">
    <span class="badge__dot"></span>
    <span class="badge__name">Caldwen</span>
  </div>

  <h1 class="main-sign__title">Caldwen Primary School<br>Ysgol Gynradd Caldwen</h1>
  <p class="main-sign__motto">Wings to fly, Roots to Grow</p>

  <div class="contact-band">
    <svg width="40" height="40" viewBox="0 0 40 40" aria-hidden="true">
      <circle cx="20" cy="20" r="20" fill="var(--white)"/>
      <path d="M13 10c1-1 2.5-1 3.2.2l2 3.2c.5.9.3 1.9-.4 2.5l-1.4 1.2c1 2.4 2.8 4.3 5.2 5.4l1.3-1.4c.7-.7 1.7-.8 2.5-.3l3.2 2c1.1.7 1.2 2.3.2 3.2l-1.7 1.6c-1.4 1.3-3.5 1.5-5.2.6-5-2.7-8.6-6.5-11-11.6-.8-1.7-.4-3.7.9-5Z" fill="var(--outdoor-green)"/>
    </svg>
    <span class="contact-band__phone">01632 960417</span>
    <div class="council-mark">Bryndale<span class="council-mark__square"></span>Council</div>
  </div>
</section>

<section class="panel-grid">
  <article class="panel">
    <h2 class="panel__school">Caldwen Primary School</h2>
    <p class="panel__message">Breakfast Club</p>
    <svg class="panel__arrow" viewBox="0 0 46 34" aria-hidden="true"><path d="M17 0 0 17l17 17h11L16 21h30v-8H16L28 0Z" fill="var(--sun-yellow)"/></svg>
  </article>
  <article class="panel">
    <h2 class="panel__school">Caldwen Primary School</h2>
    <p class="panel__message">Please use intercom to contact office</p>
    <svg class="panel__arrow" viewBox="0 0 46 34" aria-hidden="true"><path d="M17 0 0 17l17 17h11L16 21h30v-8H16L28 0Z" fill="var(--sun-yellow)"/></svg>
  </article>
  <article class="panel">
    <h2 class="panel__school">Caldwen Primary School</h2>
    <p class="panel__message">Welcome • Croeso</p>
    <svg class="panel__arrow" viewBox="0 0 46 34" aria-hidden="true"><path d="M17 0 0 17l17 17h11L16 21h30v-8H16L28 0Z" fill="var(--sun-yellow)"/></svg>
  </article>
  <article class="panel">
    <h2 class="panel__school">Caldwen Primary School</h2>
    <p class="panel__message">All visitors, please use intercom &amp; report reception</p>
  </article>
  <article class="panel">
    <h2 class="panel__school">Caldwen Primary School</h2>
    <div class="panel__notes">
      <p>Please close gates after use</p>
      <p>No parking in front of gates</p>
      <p class="panel__notes--alert">Emergency access required at all times</p>
    </div>
  </article>
  <article class="panel">
    <h2 class="panel__school">Caldwen Primary School</h2>
    <p class="panel__message">All visitors, please use intercom &amp; report reception</p>
  </article>
</section>

</body>
</html>
```